Loopnest Ad Image for Ebook

I need someone to design a good looking loopnest ad image for my ebook. Must comply with Loopnest ad police and generate lots of clicks and opt ins. Use my 3d cover attached.

```html
<!DOCTYPE html>
<html lang="en">
<head>
<meta charset="utf-8">
<title>The Steady Writing Roadmap – Free Ebook Ad</title>
<link href="https://fonts.googleapis.com/css2?family=Montserrat:wght@300;400;600;700;800&display=swap" rel="stylesheet">
<style>
  :root {
    --blue-deep: #0f66ad;
    --blue-mid: #1a76bd;
    --blue-light: #3a94d4;
    --accent-blue: #1c84cf;
    --white: #ffffff;
    --ink: #111416;
    --spine: #1b1f24;
    --paper-shade: #e9ecef;
  }
  * { margin: 0; padding: 0; box-sizing: border-box; }
  html, body {
    width: 1200px;
    height: 628px;
    overflow: hidden;
  }
  .ad {
    position: relative;
    width: 1200px;
    height: 628px;
    overflow: hidden;
    font-family: "Montserrat", Arial, sans-serif;
    background:
      radial-gradient(ellipse 620px 480px at 960px 330px, var(--blue-light) 0%, rgba(58,148,212,0) 100%),
      linear-gradient(90deg, var(--blue-deep) 0%, var(--blue-mid) 60%, var(--blue-mid) 100%);
  }
  .offer {
    position: absolute;
    left: 0;
    top: 160px;
    width: 776px;
    text-align: center;
    color: var(--white);
  }
  .offer__lead {
    font-weight: 300;
    font-size: 106px;
    line-height: 1;
    letter-spacing: 1px;
  }
  .offer__item {
    margin-top: 10px;
    font-weight: 600;
    font-size: 53px;
    line-height: 1;
    letter-spacing: 0.3px;
  }
  .cta {
    position: absolute;
    left: 243px;
    top: 397px;
    width: 286px;
    height: 62px;
    background: var(--white);
    color: var(--blue-deep);
    font-weight: 800;
    font-size: 38px;
    line-height: 62px;
    text-align: center;
    text-decoration: none;
    letter-spacing: 0.3px;
  }
  .book {
    position: absolute;
    left: 0;
    top: 0;
  }
  .book__title-light { font-weight: 400; font-size: 17px; fill: var(--white); letter-spacing: 0.4px; }
  .book__title-bold { font-weight: 700; font-size: 21px; fill: var(--accent-blue); letter-spacing: 0.8px; }
  .book__brand { font-weight: 700; font-size: 13px; fill: var(--ink); }
</style>
</head>
<body>
<main class="ad">
  <section class="offer">
    <h1 class="offer__lead">GET THIS</h1>
    <p class="offer__item">FREE BLUEPRINT</p>
  </section>

  <a class="cta" href="#">CLICK HERE</a>

  <svg class="book" width="1200" height="628" viewBox="0 0 1200 628" aria-label="Ebook cover: The Steady Writing Roadmap">
    <defs>
      <linearGradient id="photoTone" x1="0" y1="0" x2="1" y2="1">
        <stop offset="0" stop-color="#c9d3dc"/>
        <stop offset="0.5" stop-color="#eef1f3"/>
        <stop offset="1" stop-color="#dfe4e8"/>
      </linearGradient>
      <filter id="floorShadow" x="-50%" y="-200%" width="200%" height="500%">
        <feGaussianBlur stdDeviation="8"/>
      </filter>
    </defs>

    <ellipse class="book__shadow" cx="935" cy="545" rx="150" ry="10" fill="#0a3f6d" opacity="0.45" filter="url(#floorShadow)"/>

    <polygon class="book__spine-edge" points="1058,100 1072,104 1074,542 1058,545" fill="var(--spine)"/>
    <polygon class="book__pages" points="1058,100 1063,102 1063,544 1058,545" fill="var(--paper-shade)"/>

    <polygon class="book__photo" role="img" aria-label="Photo of hands typing on a laptop showing a blog page" points="800,88 1058,100 1058,398 975,378 800,330" fill="url(#photoTone)"/>

    <polygon class="book__band" points="800,330 975,378 900,525 800,515" fill="var(--ink)"/>
    <polygon class="book__accent" points="970,378 1058,305 1058,398" fill="var(--accent-blue)"/>
    <polygon class="book__corner" points="975,378 1058,398 1058,545 900,525" fill="var(--white)"/>

    <text class="book__title-light" x="819" y="400">THE STEADY</text>
    <text class="book__title-light" x="819" y="422">WRITING</text>
    <text class="book__title-bold" x="819" y="449">ROADMAP</text>

    <rect class="book__brand-mark" x="940" y="470" width="10" height="10" fill="var(--accent-blue)"/>
    <text class="book__brand" x="955" y="480">NORTHLINE</text>
    <text class="book__brand" x="955" y="495">MEDIA</text>
  </svg>
</main>
</body>
</html>
```